I need a website built for my modeling agency company.

On our website, a user can create a profile and we will submit it to thousands of modeling agents throughout the country.

In many cases, they will receive multiple offers from modeling agencies which allows them to pick and choose the contract that is best for them to launch their modeling career.

Some tag lines to consider using:

"Submit your profile to hundreds of modeling agents instantly!"

"Get found and become a star!"

We are: The Runway Guild.

Our Slogan: The World''s Largest Network of Fashion Models and Agents

What We Do: We are an agency with one of the largest networks of fashion professionals that are looking for new modeling talent. We host professional profiles for aspiring models, professional fashion models seeking work, modeling talent seekers, and top modeling agencies. We connect aspiring models with the top modeling agencies in the United States and abroad.

By submitting your FREE profile, you will be instantly introduced to the industry’s leading modeling agents. Within a few days, you could receive multiple, competing offers from modeling agencies that all want to launch your modeling career. Receiving multiple signing offers puts you in control of deciding which contract best suites you!

Reason: I've seen some good designs, but none that are 100% perfect. These are the ones that I like best so far (to give you some ideas): http://files.pixelvane.example/img/510372/820114/820114_4917263_510372_image.jpg http://files.pixelvane.example/img/510372/829305/829305_4926851_510372_image.jpg http://files.pixelvane.example/img/510372/51847/51847_4924097_510372_image.jpg http://files.pixelvane.example/img/510372/51847/51847_4919856_510372_image.jpg http://files.pixelvane.example/img/510372/823670/823670_4920438_510372_image.jpg

Target Market(s)

Aspiring models (mostly female, but some male)

Industry/Entity Type

Modeling Agency

Colors

Designer to choose colors to be used in the design.

Requirements
Nice to have
• Somewhere in the top half of the page, I would like there to be a small form for the visitor to fill out. This form will look as follows:

Title: Instantly contact hundreds of modeling agents who are looking for new talent and could make you a star!
Fields: First Name*, Last Name*, Age, Zip Code, Email Address*, Daytime Phone, Evening Phone, Comments.

Then, there will be a "submit" button to proceed to next step of form. Just below the "submit" button, should be the following verbiage: "You will have the opportunity to upload photo(s) and provide other pertinent information in next step."

```html
<!DOCTYPE html>
<html lang="en">
<head>
<meta charset="utf-8">
<title>The Runway Guild — Get Found and Become a Star</title>
<link rel="stylesheet" href="https://fonts.googleapis.com/css2?family=Oswald:wght@500;600&family=Questrial&display=swap">
<style>
  :root {
    --pink: #ea0a80;
    --pink-deep: #c3006b;
    --white: #ffffff;
    --ink: #2b2b2b;
    --hero-dark: #3c3c3c;
    --hero-mid: #8a8a8a;
    --hero-light: #b9b9b9;
    --panel: rgba(255,255,255,0.16);
    --field-line: rgba(255,255,255,0.75);
    --footer: #474747;
    --footer-text: #d6d6d6;
    --footer-icon: #8c8c8c;
    --map: #dcdcd6;
  }
  * { box-sizing: border-box; margin: 0; padding: 0; }
  html, body { width: 790px; height: 1200px; overflow: hidden; }
  body { font-family: "Questrial", "Helvetica Neue", sans-serif; color: var(--ink); background: var(--white); position: relative; }

  .hero { position: absolute; left: 0; top: 0; width: 790px; height: 538px; overflow: hidden; }
  .hero-photo { position: absolute; inset: 0;
    background: radial-gradient(ellipse at 72% 40%, var(--hero-light) 0%, var(--hero-mid) 45%, var(--hero-dark) 100%); }

  .main-nav { position: absolute; left: 86px; top: 10px; display: flex; }
  .main-nav a { font-family: "Oswald", sans-serif; font-weight: 500; font-size: 13px; color: rgba(255,255,255,0.75); text-decoration: none; margin-right: 35px; }
  .main-nav a.is-current { color: var(--white); }

  .rule { position: absolute; left: 86px; width: 309px; height: 1px; background: rgba(255,255,255,0.45); }
  .rule-top { top: 53px; }
  .rule-bottom { top: 176px; }

  .headline { position: absolute; left: 86px; top: 57px; width: 309px; white-space: nowrap; font-family: "Oswald", sans-serif; font-weight: 600; font-size: 47px; line-height: 58px; text-transform: uppercase; color: var(--white); letter-spacing: -1.2px; }
  .headline em { font-style: normal; color: var(--pink); }

  .lead { position: absolute; left: 76px; top: 190px; width: 329px; text-align: center; color: var(--white); font-size: 13px; line-height: 18px; }

  .signup { position: absolute; left: 85px; top: 240px; width: 310px; height: 216px; background: var(--panel); padding: 14px 16px 0; }
  .signup .grid { display: grid; grid-template-columns: 128px 128px; column-gap: 14px; row-gap: 7px; }
  .signup label { display: block; font-size: 8.5px; color: var(--white); }
  .signup input { display: block; width: 128px; height: 19px; margin-top: 4px; background: transparent; border: 1px solid var(--field-line); }
  .signup button { position: absolute; left: 157px; top: 142px; width: 129px; height: 24px; background: var(--pink); color: var(--white); border: 0; font-family: "Questrial", sans-serif; font-size: 12px; letter-spacing: 0.5px; }
  .signup .note { position: absolute; left: 12px; right: 12px; top: 178px; text-align: center; color: var(--white); font-size: 10px; line-height: 14px; }

  .brand { position: absolute; display: flex; align-items: center; gap: 8px; font-family: "Questrial", sans-serif; font-size: 15px; color: var(--white); letter-spacing: 0.5px; }
  .brand .mark { width: 14px; height: 14px; background: var(--pink); }
  .hero .brand { left: 94px; top: 487px; }

  .slider-dots { position: absolute; left: 331px; top: 511px; display: flex; gap: 10px; }
  .slider-dots span { width: 13px; height: 13px; border-radius: 50%; border: 1px solid rgba(255,255,255,0.7); }
  .slider-dots span.is-active { background: var(--pink); border-color: var(--white); }

  .photo-credit { position: absolute; left: 537px; top: 515px; font-size: 10px; color: rgba(255,255,255,0.7); }

  .benefits { position: absolute; left: 0; top: 538px; width: 790px; height: 165px; background: var(--pink); }
  .benefit { position: absolute; top: 0; height: 165px; display: flex; align-items: center; justify-content: center; text-align: center; color: var(--white); font-size: 19px; line-height: 22px; text-transform: uppercase; }
  .benefit.is-active { background: var(--pink-deep); }
  .benefit-pointer { position: absolute; left: 289px; top: 703px; }

  .intro { position: absolute; left: 0; top: 764px; width: 790px; text-align: center; }
  .intro h1 { font-family: "Questrial", sans-serif; font-weight: 700; font-size: 18px; color: var(--pink); -webkit-text-stroke: 0.3px var(--pink); }
  .intro p { margin: 26px auto 0; width: 590px; font-size: 13.5px; line-height: 19px; color: var(--ink); }
  .intro p a { color: var(--pink); text-decoration: none; }

  .site-footer { position: absolute; left: 0; top: 972px; width: 790px; height: 228px; background: var(--footer); box-shadow: 0 -6px 14px rgba(0,0,0,0.18); }
  .site-footer .brand { left: 90px; top: 24px; }
  .footer-rule { position: absolute; height: 1px; background: rgba(255,255,255,0.5); }
  .map { position: absolute; left: 82px; top: 107px; width: 240px; height: 80px; background: var(--map); }
  .address { position: absolute; left: 342px; top: 110px; font-size: 12.5px; line-height: 16px; color: var(--footer-text); font-style: normal; }
  .address .email { margin-top: 16px; }
  .find-us { position: absolute; left: 656px; top: 44px; font-size: 12.5px; color: var(--footer-text); }
  .social { position: absolute; left: 586px; top: 92px; display: flex; gap: 19px; }
  .social span { width: 20px; height: 20px; border-radius: 50%; background: var(--footer-icon); }
</style>
</head>
<body>

<header class="hero">
  <div class="hero-photo" role="img" aria-label="Black and white photograph of a young model seated, long wavy hair, looking at the camera"></div>

  <nav class="main-nav">
    <a class="is-current" href="#">Home</a>
    <a href="#">About</a>
    <a href="#">Models</a>
    <a href="#">My Profile</a>
    <a href="#">Blog</a>
  </nav>

  <div class="rule rule-top"></div>
  <h2 class="headline"><em>Get found</em> and<br>become <em>a star!</em></h2>
  <div class="rule rule-bottom"></div>

  <p class="lead">Instantly contact hundreds of modeling agents who are looking for new talent and could make you a star!</p>

  <form class="signup">
    <div class="grid">
      <label>First Name<input type="text"></label>
      <label>Last Name<input type="text"></label>
      <label>Age<input type="text"></label>
      <label>Zip code<input type="text"></label>
      <label>E mail adress<input type="text"></label>
      <label>Phone<input type="text"></label>
    </div>
    <button type="button">BE THE ONE</button>
    <p class="note">You will have the opportunity to upload photo(s) and provide other pertinent information in next step.*</p>
  </form>

  <div class="brand"><span class="mark"></span>The Runway Guild</div>

  <div class="slider-dots"><span></span><span></span><span class="is-active"></span></div>
  <p class="photo-credit">This picture belongs to Mara Velloni</p>
</header>

<section class="benefits">
  <div class="benefit" style="left:0;width:223px;">Free<br>online<br>profile</div>
  <div class="benefit is-active" style="left:223px;width:172px;">Instantly<br>to fashion<br>world</div>
  <div class="benefit" style="left:395px;width:171px;">Lounch<br>modeling<br>career</div>
  <div class="benefit" style="left:566px;width:224px;">Become<br>a super<br>star</div>
</section>
<svg class="benefit-pointer" width="44" height="22" viewBox="0 0 44 22" aria-hidden="true"><polygon points="0,0 44,0 22,22" fill="#c3006b"/></svg>

<section class="intro">
  <h1>Submit your profile to hundreds of modeling agents instantly!</h1>
  <p>By submitting your <a href="#">FREE profile</a>, you will be instantly introduced to the industry’s <a href="#">leading modeling agents</a>. Within a few days, you could receive multiple, competing offers from modeling agencies that all want to launch your <a href="#">modeling career</a>. Receiving multiple signing offers puts you in control of deciding which contract best suites you!</p>
</section>

<footer class="site-footer">
  <div class="brand"><span class="mark"></span>The Runway Guild</div>
  <div class="footer-rule" style="left:85px;top:79px;width:105px;"></div>

  <div class="map" role="img" aria-label="Street map showing the office location"></div>
  <address class="address">
    Street<br>Zip code<br>Countruy
    <div class="email">E mail</div>
  </address>

  <p class="find-us">Find us on</p>
  <div class="footer-rule" style="left:618px;top:72px;width:104px;"></div>
  <div class="social" aria-label="Social network links"><span></span><span></span><span></span><span></span></div>
</footer>

</body>
</html>
```